Medical Device Packaging Project 2 of 5

We are a medical device startup company needing packaging for a total of 5 device brands. This is posting 2 of 5 and the device name is "Velmora"

Velmora is an intraocular lens for use in cataract surgery. The target market is Chinese ophthalmologists. The box should be sophisticated and upmarket.

The company name is Brindle Optics, I have included the logo in the uploaded files section. You should include the logo on the box.

I have uploaded a sample lens boxes from other companies that demonstrate the information needed to be contained on the box in terms of address, warnings, symbols, etc.

I have also uploaded the blank dieline of the boxes

You are welcome and encouraged to also submit to projects 1, 3, 4, and 5 as well. The same rules and expectations apply.

Requirements
Should not have
• Should not have any images of an eye or any bionic/futuristic feel to the design
• Note that the vantiscope box is for text reference only. You may use the lens image but the futuristic/bionic look is NOT what we are going for with this brand. It should be traditional upmarket medical device artwork.

```html
<!DOCTYPE html>
<html lang="en">
<head>
<meta charset="utf-8">
<title>Velmora Intraocular Lens – Box Artwork</title>
<link rel="stylesheet" href="https://fonts.googleapis.com/css2?family=Montserrat:wght@400;500;600&family=Arimo:wght@400&display=swap">
<style>
  :root {
    --stage: #ececec;
    --paper: #fdfbfb;
    --blush: #f6d3d6;
    --blush-deep: #f0bfc4;
    --mauve: #9a6a70;
    --navy: #1f4a7d;
    --sky: #a9cfe6;
    --body-text: #8c7176;
    --steel-light: #f2f2f2;
    --steel: #a8a8a8;
    --steel-dark: #6f6f6f;
  }
  * { box-sizing: border-box; margin: 0; padding: 0; }
  html, body { width: 1200px; height: 782px; overflow: hidden; }
  body {
    background: var(--stage);
    font-family: "Montserrat", sans-serif;
    position: relative;
  }
  .panel {
    position: absolute;
    top: 186px;
    width: 550px;
    height: 410px;
    background: var(--paper);
    overflow: hidden;
    box-shadow: 0 2px 8px rgba(0,0,0,0.08);
  }
  .panel--back { left: 35px; }
  .panel--front { left: 615px; }

  .wash {
    position: absolute;
    inset: 0;
    background:
      radial-gradient(ellipse 70% 55% at 70% 85%, var(--blush-deep) 0%, rgba(240,191,196,0) 70%),
      radial-gradient(ellipse 60% 45% at 20% 95%, var(--blush) 0%, rgba(246,211,214,0) 75%),
      linear-gradient(180deg, rgba(253,251,251,1) 0%, rgba(253,251,251,1) 30%, rgba(248,222,225,0.9) 70%, rgba(246,211,214,1) 100%);
  }

  .brand {
    position: absolute;
    left: 34px;
    top: 92px;
    display: flex;
    align-items: center;
    gap: 8px;
  }
  .brand__mark {
    width: 12px; height: 12px;
    border-radius: 50%;
    background: var(--sky);
  }
  .brand__name {
    font-weight: 500;
    font-size: 20px;
    letter-spacing: 0.5px;
    color: var(--navy);
    white-space: nowrap;
  }

  .headline {
    position: absolute;
    right: 24px;
    top: 62px;
    width: 270px;
    text-align: right;
    font-weight: 500;
    font-size: 13px;
    line-height: 18px;
    letter-spacing: 0.2px;
    color: var(--mauve);
    text-transform: uppercase;
  }

  .lens-art {
    position: absolute;
    background: radial-gradient(closest-side at 50% 50%, var(--steel-light) 0%, var(--steel) 55%, rgba(168,168,168,0.35) 85%, rgba(168,168,168,0) 100%);
  }
  .panel--back .lens-art { left: 320px; top: 130px; width: 190px; height: 150px; }
  .panel--front .lens-art { left: 280px; top: 110px; width: 240px; height: 200px; }

  .notices {
    position: absolute;
    left: 32px;
    top: 140px;
    width: 250px;
    font-family: "Arimo", sans-serif;
    font-size: 7px;
    line-height: 8px;
    color: var(--body-text);
  }
  .notices p { margin-bottom: 3px; }

  .symbols {
    position: absolute;
    right: 28px;
    bottom: 36px;
    display: flex;
    gap: 8px;
    align-items: center;
  }
  .symbols svg { display: block; }

  .product {
    position: absolute;
    left: 34px;
    bottom: 30px;
  }
  .product__name {
    font-weight: 600;
    font-size: 24px;
    letter-spacing: 5px;
    color: var(--steel-dark);
    text-transform: uppercase;
    line-height: 28px;
  }
  .product__tagline {
    font-weight: 500;
    font-size: 13px;
    letter-spacing: 0.2px;
    color: var(--mauve);
    text-transform: uppercase;
  }
</style>
</head>
<body>

  <section class="panel panel--back" aria-label="Box back panel">
    <div class="wash"></div>
    <div class="brand">
      <span class="brand__mark"></span>
      <span class="brand__name">Brindle Optics</span>
    </div>
    <h2 class="headline">Hydrophobic intraocular lens<br>Aspheric with 360° lens</h2>
    <div class="lens-art" role="img" aria-label="Illustration of an intraocular lens with C-loop haptics"></div>

    <div class="notices">
      <p>Contains one sterile intraocular lens<br>Do not use if the packaging is damaged<br>Do not resterilize</p>
      <p>Bevat één steriele intraoculaire lens<br>Niet gebruiken als de verpakking beschadigd is<br>Niet opnieuw steriliseren</p>
      <p>Contient une lentille intraoculaire stérile<br>Ne pas utiliser si l'emballage est endommagé<br>Ne pas restériliser</p>
      <p>Enthält eine sterile intraokulare Linse<br>Nicht verwenden, wenn die Verpackung beschädigt ist<br>Nicht resterilisieren</p>
      <p>Periéchei éna aposteiroméno endofthálmio fakó<br>Περιέχει ένα αποστειρωμένο ενδοφθάλμιο φακό<br>Μην το χρησιμοποιείτε εάν η συσκευασία έχει υποστεί ζημιά<br>Μην επαναποστειρώνετε</p>
      <p>Contiene una lente intraoculare sterile<br>Non usare se la confezione è danneggiata<br>Non risterilizzare</p>
      <p>Contém uma lente intra-ocular esterilizada<br>Não use se a embalagem está danificada<br>Não reesterilize</p>
      <p>Contiene una lente intraocular estéril<br>No utilizar si el envase está dañado<br>No vuelva a esterilizar</p>
    </div>

    <div class="symbols" aria-label="Regulatory symbols">
      <svg width="46" height="16" viewBox="0 0 46 16" aria-label="Sterile EO">
        <rect x="0.5" y="0.5" width="45" height="15" fill="none" stroke="var(--body-text)"/>
        <line x1="33" y1="0.5" x2="33" y2="15.5" stroke="var(--body-text)"/>
        <text x="16.5" y="10.5" font-size="6.5" font-family="Arimo, sans-serif" text-anchor="middle" fill="var(--body-text)">STERILE</text>
        <text x="39.5" y="10.5" font-size="6.5" font-family="Arimo, sans-serif" text-anchor="middle" fill="var(--body-text)">EO</text>
      </svg>
      <svg width="18" height="16" viewBox="0 0 18 16" aria-label="Caution">
        <path d="M9 1 L17 15 H1 Z" fill="none" stroke="var(--body-text)"/>
        <line x1="9" y1="6" x2="9" y2="11" stroke="var(--body-text)"/>
        <circle cx="9" cy="13" r="0.7" fill="var(--body-text)"/>
      </svg>
      <svg width="16" height="16" viewBox="0 0 16 16" aria-label="Do not reuse">
        <circle cx="8" cy="8" r="7" fill="none" stroke="var(--body-text)"/>
        <line x1="3" y1="13" x2="13" y2="3" stroke="var(--body-text)"/>
      </svg>
      <svg width="16" height="16" viewBox="0 0 16 16" aria-label="Do not resterilize">
        <circle cx="8" cy="8" r="7" fill="none" stroke="var(--body-text)"/>
        <line x1="3" y1="13" x2="13" y2="3" stroke="var(--body-text)"/>
        <rect x="4.5" y="5.5" width="7" height="5" fill="none" stroke="var(--body-text)" stroke-width="0.8"/>
      </svg>
      <svg width="16" height="16" viewBox="0 0 16 16" aria-label="Do not use if package is damaged">
        <circle cx="8" cy="8" r="7" fill="none" stroke="var(--body-text)"/>
        <rect x="4.5" y="5" width="7" height="6" fill="none" stroke="var(--body-text)" stroke-width="0.8"/>
        <line x1="3" y1="13" x2="13" y2="3" stroke="var(--body-text)"/>
      </svg>
    </div>
  </section>

  <section class="panel panel--front" aria-label="Box front panel">
    <div class="wash"></div>
    <div class="brand">
      <span class="brand__mark"></span>
      <span class="brand__name">Brindle Optics</span>
    </div>
    <h2 class="headline">Hydrophobic intraocular lens</h2>
    <div class="lens-art" role="img" aria-label="Illustration of an intraocular lens with C-loop haptics"></div>
    <div class="product">
      <h1 class="product__name">Velmora</h1>
      <p class="product__tagline">Aspheric with 360° lens</p>
    </div>
  </section>

</body>
</html>
```